Trucking company specializing in intermodal containers

We need a logo design for our trucking company based in Kent, Washington. Our companies name is Dorvale Haulworks LLC, we specialize in intermodal containers, and work off of the Crestmark rail lines and the ports. We provide service by transporting freight with our fleet of trucks. We operate within Washington, Oregon, and Idaho. Our fleet consists of an east division and a local division. Our team motto currently is globally connected, locally invested.

Target Market(s)

brokers, intermodal management companies, customers

Industry/Entity Type

Trucking Company

Contact Information for Business Card

physical address 4519 N. 163rd Pl Kent, WA 98517
office number is 253-614-9026

Font styles to use
Sans Serif

Colors

Designer to choose colors to be used in the design.

Requirements
Must have
• We need to update our current logo. Something like an emblem; that makes a statement that this logo/ sign represents Dorvale Haulworks. Something like a royal stamp but in this case a royal shield.
Nice to have
• simple, yet bold. something someone does not currently have. We need something fresh and exciting. Something that will also make a statement because currently our reputation is great within the industry and our community. But we need to reflect that we are professional and willing to provide the best service. We are open to new statement lines.
Should not have
• Should not have something thats been used before. We are open to suggestions that you have and a design that is completely unique and you make originally without what we want but what you like as well. Ofcourse it should still represent the industry we are in.

```html
<!DOCTYPE html>
<html lang="en">
<head>
<meta charset="utf-8">
<title>Dorvale Haulworks LLC – Business Card</title>
<link href="https://fonts.googleapis.com/css2?family=Source+Sans+3:wght@400;700&display=swap" rel="stylesheet">
<style>
  :root {
    --brand-red: #d40000;
    --ink: #111111;
    --card-white: #ffffff;
    --card-black: #000000;
    --stage-light: #e2e2e2;
    --stage-dark: #b0b0b0;
  }
  * { margin: 0; padding: 0; box-sizing: border-box; }
  html, body { width: 1200px; height: 1200px; overflow: hidden; }
  body {
    position: relative;
    font-family: "Source Sans 3", "Myriad Pro", Arial, sans-serif;
    background: radial-gradient(ellipse at 50% 50%, var(--stage-light) 0%, var(--stage-dark) 62%, #a9a9a9 100%);
    color: var(--ink);
  }
  .card {
    position: absolute;
    left: 216px;
    width: 796px;
    height: 453px;
    overflow: hidden;
  }
  .card--front { top: 135px; background: var(--card-white); }
  .card--back { top: 614px; background: var(--card-black); border: 1px solid #7a1010; }

  /* Front */
  .front-brand { position: absolute; left: 38px; top: 31px; display: flex; align-items: center; gap: 16px; }
  .brand-dot { width: 86px; height: 86px; border-radius: 50%; background: var(--brand-red); flex: none; }
  .brand-name {
    color: var(--brand-red);
    font-weight: 700;
    text-transform: uppercase;
    line-height: 1;
  }
  .brand-name .line-main { display: block; font-size: 54px; letter-spacing: 1px; }
  .brand-name .line-sub { display: block; font-size: 24px; letter-spacing: 2.5px; margin-top: 4px; }

  .holder { position: absolute; left: 45px; top: 208px; }
  .holder-name { font-size: 32px; font-weight: 700; line-height: 1.1; }
  .holder-title { font-size: 23px; font-weight: 400; margin-top: 4px; }

  .contact { position: absolute; left: 432px; top: 138px; font-size: 23px; line-height: 30px; }
  .contact-row { display: flex; }
  .contact-label { width: 27px; }
  .contact-value { padding-left: 4px; }
  .contact-gap { height: 20px; }
  .contact-gap-small { height: 18px; }

  .stripe-red { position: absolute; left: 0; top: 381px; width: 100%; height: 12px; background: var(--brand-red); }
  .stripe-black { position: absolute; left: 0; top: 402px; width: 100%; height: 51px; background: var(--card-black); }

  /* Back */
  .back-brand { position: absolute; left: 82px; top: 115px; display: flex; align-items: center; gap: 28px; }
  .back-brand .brand-dot { width: 154px; height: 154px; }
  .back-brand .brand-name { color: var(--card-white); }
  .back-brand .line-main { font-size: 98px; letter-spacing: 2px; }
  .back-brand .line-sub { font-size: 42px; letter-spacing: 4px; margin-top: 6px; }
  .back-brand .brand-dot { background: var(--card-white); }

  .back-web {
    position: absolute; left: 0; right: 0; top: 368px;
    text-align: center;
    color: var(--card-white);
    font-size: 26px;
    letter-spacing: 13px;
    padding-left: 13px;
  }
</style>
</head>
<body>
  <section class="card card--front">
    <div class="front-brand">
      <span class="brand-dot"></span>
      <div class="brand-name">
        <span class="line-main">Dorvale</span>
        <span class="line-sub">Haulworks LLC</span>
      </div>
    </div>

    <div class="holder">
      <p class="holder-name">Your Full Name</p>
      <p class="holder-title">Your Title</p>
    </div>

    <div class="contact">
      <div class="contact-row"><span class="contact-label">A</span><span class="contact-value">: 4519 N. 163rd Pl Kent,<br>&nbsp;&nbsp;WA 98517</span></div>
      <div class="contact-gap"></div>
      <div class="contact-row"><span class="contact-label">P</span><span class="contact-value">: 253-614-9026</span></div>
      <div class="contact-row"><span class="contact-label">M</span><span class="contact-value">: 012-345-6789</span></div>
      <div class="contact-row"><span class="contact-label">E</span><span class="contact-value">: your email address</span></div>
      <div class="contact-gap-small"></div>
      <div class="contact-row"><span class="contact-label">W</span><span class="contact-value">: www.dorvalehaulworks.com</span></div>
    </div>

    <div class="stripe-red"></div>
    <div class="stripe-black"></div>
  </section>

  <section class="card card--back">
    <div class="back-brand">
      <span class="brand-dot"></span>
      <div class="brand-name">
        <span class="line-main">Dorvale</span>
        <span class="line-sub">Haulworks LLC</span>
      </div>
    </div>
    <p class="back-web">www.dorvalehaulworks.com</p>
  </section>
</body>
</html>
```